Business card design needed

We need a business card design and possible logo for my new building construction business. I would like a masculine type of business design.

Thanks
Also can we please put my ABN number 48305927164 in as well thanks.
And use the colours black, orange and white. Cheers

Industry/Entity Type

Building

Contact Information for Business Card

Darnock constructions, owner: Corwin tate, mobile:0418207736, email: tatey.c@fernmail.example, licence: 617403D

```html
<!DOCTYPE html>
<html lang="en">
<head>
<meta charset="utf-8">
<title>Darnock construction company – Business Card</title>
<link rel="stylesheet" href="https://fonts.googleapis.com/css2?family=Tinos:wght@400&display=swap">
<style>
  :root {
    --orange-light: #ffb443;
    --orange-mid: #ff7a2a;
    --orange-deep: #ff4a24;
    --swoosh: #ff5a14;
    --ring: #ff8a1e;
    --badge-fill: #fde3d8;
    --ink: #111111;
  }
  html, body {
    margin: 0;
    padding: 0;
    width: 1200px;
    height: 688px;
    overflow: hidden;
    background: #ffffff;
  }
  .card {
    position: relative;
    width: 1200px;
    height: 688px;
    overflow: hidden;
    background: linear-gradient(100deg, var(--orange-light) 0%, var(--orange-mid) 45%, var(--orange-deep) 100%);
    font-family: "Tinos", "Times New Roman", serif;
    color: var(--ink);
    box-shadow: inset 0 0 0 2px #2a2a2a;
  }
  .card__swoosh {
    position: absolute;
    inset: 0;
    width: 1200px;
    height: 688px;
  }
  .owner-name {
    position: absolute;
    left: 84px;
    top: 44px;
    margin: 0;
    font-size: 60px;
    font-weight: 400;
    line-height: 1;
    white-space: nowrap;
    text-shadow: 1px 1px 2px rgba(0,0,0,0.35);
  }
  .owner-role {
    position: absolute;
    right: 736px;
    top: 110px;
    margin: 0;
    font-size: 46px;
    line-height: 1;
    white-space: nowrap;
    text-shadow: 1px 1px 2px rgba(0,0,0,0.3);
  }
  .contact {
    margin: 0;
    font-size: 47px;
    line-height: 1;
    text-shadow: 1px 1px 2px rgba(0,0,0,0.3);
  }
  .contact__line {
    position: absolute;
    left: 34px;
    white-space: nowrap;
  }
  .contact__line--mobile { top: 420px; }
  .contact__line--licence { top: 474px; }
  .contact__line--abn { top: 528px; }
  .contact__line--email { top: 594px; }
  .brand-badge {
    position: absolute;
    left: 603px;
    top: 94px;
    width: 524px;
    height: 524px;
    box-sizing: border-box;
    border-radius: 50%;
    border: 14px solid var(--ring);
    background: var(--badge-fill);
    display: flex;
    align-items: center;
    justify-content: center;
    text-align: center;
  }
  .brand-badge__name {
    margin: 0;
    font-size: 48px;
    font-weight: 400;
    line-height: 1.2;
    color: var(--ink);
  }
</style>
</head>
<body>
  <div class="card">
    <svg class="card__swoosh" viewBox="0 0 1200 688" aria-hidden="true">
      <defs>
        <linearGradient id="swooshFade" x1="0" y1="1" x2="1" y2="0">
          <stop offset="0" stop-color="var(--swoosh)" stop-opacity="0.15"/>
          <stop offset="0.5" stop-color="var(--swoosh)" stop-opacity="0.85"/>
          <stop offset="1" stop-color="var(--swoosh)" stop-opacity="0.6"/>
        </linearGradient>
      </defs>
      <path d="M0 392 C 180 400, 320 330, 420 190 C 500 80, 640 10, 830 0 L 770 0 C 600 20, 480 90, 400 200 C 310 330, 170 385, 0 392 Z"
            fill="url(#swooshFade)"/>
    </svg>

    <h1 class="owner-name">Corwin Tate</h1>
    <p class="owner-role">proprietor</p>

    <p class="contact">
      <span class="contact__line contact__line--mobile">Mobile # 0418207736</span>
      <span class="contact__line contact__line--licence">Licence#&nbsp; 617403D</span>
      <span class="contact__line contact__line--abn">ABN# 48305927164</span>
      <span class="contact__line contact__line--email">Email- tatey.c@fernmail.example</span>
    </p>

    <div class="brand-badge">
      <p class="brand-badge__name">Darnock<br>construction<br>company</p>
    </div>
  </div>
</body>
</html>
```